ALL TEXT GRAPHICS TM May 2025 for Instagram

We are looking for a series of social media graphics for Instagram (new size: 4:5 (1080 x 1350 pixels) ratio that are ALL TEXT. We want the following quotes below on each graphic; one quote per graphic. AND, In very small letters at the bottom of each graphic, add @TovaMarshOnline
The look and feel of these graphics should be complimentary to the color palette attached below; but keep them simple. But the design is up to you; at the end of this document, I provided various samples of all text graphics that I like as examples.
Target Market(s)
women looking to lose weight
Look and feel

```html
<!DOCTYPE html>
<html lang="en">
<head>
<meta charset="utf-8">
<title>All Text Graphics – TM Instagram Series</title>
<link href="https://fonts.googleapis.com/css2?family=Barlow+Condensed:wght@600&family=Open+Sans:wght@300&display=swap" rel="stylesheet">
<style>
  :root {
    --page-bg: #ffffff;
    --edge-dark: #1f1a1c;
    --mid-magenta: #8a0f4c;
    --core-pink: #ff0a82;
    --text-light: #e9e6e7;
  }
  * { margin: 0; padding: 0; box-sizing: border-box; }
  html, body {
    width: 1200px;
    height: 811px;
    overflow: hidden;
    background: var(--page-bg);
  }
  .series {
    position: relative;
    width: 1200px;
    height: 811px;
  }
  .post {
    position: absolute;
    width: 344px;
    height: 430px;
    background: radial-gradient(ellipse 62% 58% at 50% 50%,
      var(--core-pink) 0%,
      #d4066c 30%,
      var(--mid-magenta) 62%,
      var(--edge-dark) 100%);
    color: var(--text-light);
  }
  .post--one   { left: 47px;  top: 198px; }
  .post--two   { left: 427px; top: 194px; }
  .post--three { left: 790px; top: 193px; }

  .quote {
    position: absolute;
    font-family: "Barlow Condensed", "Arial Narrow", sans-serif;
    font-weight: 600;
    text-transform: uppercase;
    white-space: nowrap;
    letter-spacing: -0.2px;
  }
  .post--one .quote   { left: 48px; top: 161px; font-size: 31px; line-height: 27.5px; }
  .post--two .quote   { left: 51px; top: 68px;  font-size: 39px; line-height: 42px; }
  .post--three .quote { left: 78px; top: 50px;  font-size: 37px; line-height: 37.4px; }
  .quote .indent { padding-left: 8px; }

  .handle {
    position: absolute;
    left: 0;
    width: 100%;
    text-align: center;
    font-family: "Open Sans", sans-serif;
    font-weight: 300;
    font-size: 11.5px;
    letter-spacing: 0.2px;
  }
  .post--one .handle   { top: 293px; padding-left: 16px; }
  .post--two .handle   { top: 382px; }
  .post--three .handle { top: 395px; padding-left: 14px; }
</style>
</head>
<body>
  <main class="series">
    <section class="post post--one">
      <p class="quote">Tired. Moody. Stubborn<br>belly fat your hormones<br>are screaming for help!<br>Let’s fix that.</p>
      <p class="handle">@TovaMarshOnline</p>
    </section>

    <section class="post post--two">
      <p class="quote">That stubborn<br>weight?<br>It’s not your fault.<br>Your hormones are<br>to blame and<br>you’re not alone;<br><span class="indent">but there is a fix.</span></p>
      <p class="handle">@TovaMarshOnline</p>
    </section>

    <section class="post post--three">
      <p class="quote">Your belly isn’t<br>fat . . .<br>It’s hormonal.<br>And here’s<br>how to fix it.<br>Comment<br>hormones<br>if nothing is<br>working.</p>
      <p class="handle">@TovaMarshOnline</p>
    </section>
  </main>
</body>
</html>
```